Event branding Sales presentation PowerPoint template required

We are looking to freshen up & step up the professional quality of our powerpoint presentation template. I am looking for a professional designer with good creative background to design a new template for our presentations to new clients and for bespoke projects.
We have attached our current PPP as well as an elevator pitch which has most of the information we would like on the template

We have 3 main parts of our business which are:
- Event Branding
- Fan Engagements
- Set builds / Theming

Target Market(s)

Event organisers and sporting fedrations

Industry/Entity Type

Events

Requirements
Must have
• Ability for easy editing. Strong visual representation
Nice to have
• Information pages as well as look-book pages
Should not have
• Overcrowded graphics / arty graphics

```html
<!DOCTYPE html>
<html lang="en">
<head>
<meta charset="utf-8">
<title>Summit Events – Business Marketing Presentation</title>
<link href="https://fonts.googleapis.com/css2?family=Roboto:wght@400;500;700;900&family=Montserrat:wght@300;400;600&display=swap" rel="stylesheet">
<style>
:root{
  --bg-wood:#a98a3e;
  --bg-wood-dark:#94762f;
  --slide:#1b1b1b;
  --slide-2:#262523;
  --gold:#c9a44c;
  --gold-light:#e2c677;
  --gold-deep:#9d7a2c;
  --grey:#9a9a9a;
  --white:#f3f1ec;
  --text:#d9d6cf;
}
*{box-sizing:border-box;margin:0;padding:0}
html,body{width:1028px;height:1200px;overflow:hidden}
body{background:linear-gradient(160deg,var(--bg-wood) 0%,#b3934a 45%,var(--bg-wood-dark) 100%);font-family:"Roboto",Arial,sans-serif;color:var(--text);position:relative}
.slide{position:absolute;width:300px;height:168px;background:radial-gradient(ellipse at 30% 20%,var(--slide-2),var(--slide) 70%);box-shadow:2px 3px 6px rgba(0,0,0,.45);overflow:hidden}
.slide > *{position:absolute}
.c1{left:42px}.c2{left:366px}.c3{left:689px}
.r1{top:45px}.r2{top:233px}.r3{top:420px}.r4{top:609px}.r5{top:797px}.r6{top:987px}

.mark{right:14px;top:7px;width:34px;text-align:center}
.mark i{display:block;width:13px;height:13px;margin:0 auto 1px;border:.7px solid var(--grey);border-radius:50%}
.mark b{display:block;font:400 2.6px "Montserrat",sans-serif;letter-spacing:.5px;color:var(--grey);white-space:nowrap}
.foot{right:8px;bottom:5px;font:400 5.6px "Montserrat",sans-serif;letter-spacing:1.6px;color:var(--gold);display:flex;align-items:center;gap:2px}
.foot span{background:var(--gold);color:#1b1b1b;font-size:3px;letter-spacing:0;padding:0 2px;line-height:4px}

.title{left:15px;top:12px;font:700 14px/1 "Roboto",sans-serif;color:var(--white);white-space:nowrap}
.title em{font-style:normal;color:var(--gold)}
.title.gold{color:var(--gold)}
.title .w{color:var(--white)}
.sub{left:19px;top:31px;font:400 6.8px "Roboto",sans-serif;color:var(--white);white-space:nowrap}
.ph{border:1px solid var(--gold-deep)}

/* cover */
.cover-band{left:0;top:97px;width:300px;height:71px;background:linear-gradient(100deg,#9d7c33,#d8bb70 45%,#b8953f)}
.cover-logo{left:16px;top:15px;width:100px;text-align:center}
.cover-logo i{display:block;width:38px;height:38px;margin:0 auto 4px;border:1.2px solid var(--gold);border-radius:50%}
.cover-logo b{font:400 7px "Montserrat",sans-serif;letter-spacing:1.6px;color:var(--gold-light);white-space:nowrap}
.cover-photo-main{left:125px;top:26px;width:168px;height:81px;border:3px solid var(--gold);background:linear-gradient(180deg,#6f8090 0%,#5f7a50 40%,#2f5ea8 70%,#3c6b3a)}
.cover-photo-side{left:16px;top:84px;width:97px;height:74px;border:3px solid var(--gold);background:linear-gradient(180deg,#b9c2c7 0%,#9aa5a8 45%,#d64f63 60%,#5f8a3e 80%)}
.cover-kicker{left:235px;top:115px;font:500 7px "Roboto",sans-serif;color:#2b2208}
.cover-title{left:203px;top:122px;font:900 16.5px/1 "Roboto",sans-serif;color:#f4e9c8}
.cover-title span{display:block;color:#8a6a22;font-size:14.5px;margin-top:1px}
.badge{top:124px;width:29px;height:29px;background:#151515}
.badge.a{left:130px}.badge.b{left:164px}

/* list boxes */
.toc{left:15px;top:43px;width:132px;height:97px;border:.7px solid var(--gold-deep)}
.toc-item{width:122px}
.toc-item h4{font:500 6.6px "Roboto",sans-serif;color:var(--gold)}
.toc-item h4 b{font-weight:700;margin-right:3px}
.toc-item p{font:400 3.6px/1.35 "Roboto",sans-serif;color:var(--text);margin:2px 0 0 11px}

/* about */
.welcome{left:11px;top:43px;width:277px;height:19px;background:var(--gold);color:#111;font:700 10.5px/19px "Roboto",sans-serif;text-align:center}
.welcome-box{left:11px;top:62px;width:277px;height:75px;border:.7px solid var(--gold-deep);padding:4px 4px;font:400 3.6px/1.5 "Roboto",sans-serif;color:var(--text)}
.welcome-box p{margin-bottom:3px}
.hl{color:var(--gold)}
.welcome-box .center{text-align:center;margin-top:4px}

/* unique perspective */
.up-gold{left:0;top:40px;width:140px;height:128px;background:linear-gradient(160deg,#1b1b1b 20%,#6f5620 55%,#c9a44c)}
.up-photo{left:10px;top:50px;width:123px;height:95px;border:3px solid #0d0d0d;outline:.7px solid var(--gold-deep);background:radial-gradient(circle at 55% 40%,#c23a86 0%,#6d2a4a 35%,#2b1420 70%),#1c0c12}
.up-text{left:144px;top:52px;width:146px;font:400 4.4px/1.45 "Roboto",sans-serif;color:var(--text)}
.up-text h3{font:500 8.4px "Roboto",sans-serif;color:var(--gold);margin-bottom:4px}
.up-text p{margin-bottom:4px}

/* turnkey */
.tk-box{left:13px;top:38px;width:281px;height:80px;border:.7px solid var(--gold-deep)}
.tk-svg{left:13px;top:38px}
.tk-label{font:500 3.3px "Roboto",sans-serif;color:var(--gold);transform:translateX(-50%);text-align:center;white-space:nowrap}
.tk-label.low{color:var(--text)}
.tk-foot{left:13px;top:123px;width:275px;font:400 4.5px/1.45 "Roboto",sans-serif;color:var(--text)}
.tk-foot h4{font:700 6.4px "Roboto",sans-serif;color:var(--gold);margin-bottom:1px}

/* propositions */
.prop-head{left:0;top:10px;width:300px;text-align:center;font:900 8.6px/1.15 "Roboto",sans-serif;color:var(--white)}
.prop-head em{font-style:normal;color:var(--gold);display:block}
.prop-list{font:400 5.3px/1.4 "Roboto",sans-serif;color:var(--white);white-space:nowrap}
.prop-list h5{font:700 5.5px "Roboto",sans-serif;color:var(--gold)}
.prop-note{left:28px;top:128px;width:82px;height:21px;border:.6px solid var(--grey);padding:1px 2px;font:400 2.8px/1.3 "Roboto",sans-serif;color:var(--text)}
.prop-note b{color:var(--gold);font-weight:700}

/* service rows */
.srow{left:19px;width:254px;height:27px;border:.7px solid var(--grey);display:flex;align-items:center}
.srow .ico{width:29px;height:100%;border-right:.7px solid var(--grey);display:flex;align-items:center;justify-content:center;flex:none}
.srow .lbl{margin-left:3px;width:71px;height:12px;background:var(--gold);color:#111;font:700 7px/12px "Roboto",sans-serif;text-align:center;flex:none}
.srow .lbl.sm{font-size:4.6px}
.srow p{margin-left:5px;width:142px;font:400 3.6px/1.3 "Roboto",sans-serif;color:var(--white)}
.rule{left:19px;top:45px;width:37px;height:1px;background:var(--gold)}

/* fan engagement look */
.fe-title{left:14px;top:16px;font:700 14px/1.05 "Roboto",sans-serif;color:var(--white)}
.fe-title em{font-style:normal;color:var(--gold);display:block}
.bullets{list-style:none;color:var(--white);white-space:nowrap}
.bullets li::before{content:"";display:inline-block;width:3px;height:3px;background:var(--gold);margin-right:4px;vertical-align:middle}

/* cards */
.card{width:121px;height:50px;border:.7px solid var(--grey);display:flex;overflow:hidden}
.card.col1{left:19px}.card.col2{left:150px}
.card .pic{width:47px;height:100%;flex:none}
.card .txt{width:73px;padding:3px 3px 0 3px;font:400 3.6px/1.3 "Roboto",sans-serif;color:var(--white);text-align:justify}
.card h4{font:500 7.4px/1 "Roboto",sans-serif;color:var(--gold);margin-bottom:2px;text-align:left}

/* why */
.why-col{top:47px;height:93px;border:.7px solid var(--grey)}
.why-col h4{height:16px;background:var(--gold);color:#111;font:700 10px/16px "Roboto",sans-serif;text-align:center;margin:-.7px -.7px 0}
.why-col p{padding:4px 5px;font:400 4.1px/1.45 "Roboto",sans-serif;color:var(--white);text-align:justify}

/* install */
.inst-txt{top:112px;width:112px;font:400 4.4px/1.45 "Roboto",sans-serif;color:var(--white)}
.inst-txt h4{font:700 6.4px "Roboto",sans-serif;color:var(--gold);margin-bottom:1px}

/* contact */
.contact-frame{left:9px;top:9px;width:282px;height:150px;border:.8px solid var(--gold)}
.contact{left:0;width:300px;text-align:center;color:var(--white)}
.contact-title{top:22px;font:900 17px "Roboto",sans-serif}
.contact-rule{left:125px;top:43px;width:50px;height:1.2px;background:var(--gold)}
.contact-lead{top:50px;font:400 7px/1.1 "Roboto",sans-serif}
.contact-line{top:72px;font:400 9.5px "Montserrat",sans-serif;display:flex;justify-content:center;align-items:center;gap:2px}
.contact-web{top:86px;font:400 9.5px "Montserrat",sans-serif;letter-spacing:.5px}
.contact-web em{font-style:normal;color:var(--gold)}
.contact-thanks{top:104px;font:900 17px "Roboto",sans-serif;color:var(--gold);letter-spacing:1px}
.contact-q{top:126px;font:400 7px/1.05 "Roboto",sans-serif}
</style>
</head>
<body>

<!-- 01 cover -->
<section class="slide c1 r1">
  <div class="cover-band"></div>
  <div class="cover-logo"><i></i><b>SUMMIT EVENTS</b></div>
  <div class="cover-photo-main" role="img" aria-label="Aerial photo of an outdoor sports venue with blue branded stands"></div>
  <div class="cover-photo-side" role="img" aria-label="Photo of giant colourful 3D letters on a lawn"></div>
  <div class="badge a" role="img" aria-label="Partner badge"></div>
  <div class="badge b" role="img" aria-label="Hoop League partner badge"></div>
  <div class="cover-kicker">PRESENTATION</div>
  <div class="cover-title">BUSINESS<span>MARKETING</span></div>
</section>

<!-- 02 contents -->
<section class="slide c2 r1">
  <div class="title gold" style="top:14px;font-size:19px">Contents</div>
  <div class="mark"><i></i><b>SUMMIT EVENTS</b></div>
  <div class="toc"></div>
  <div class="toc-item" style="left:23px;top:49px"><h4><b>1.</b>About Us</h4><p>A brief overview of Summit Events</p></div>
  <div class="toc-item" style="left:23px;top:83px"><h4><b>2.</b>Unique Perspective</h4><p>What makes us different and a good supply partner to Hoop League</p></div>
  <div class="toc-item" style="left:23px;top:114px"><h4><b>3.</b>Turnkey Solutions</h4><p>From initial concept or event plan, Summit Events can manage all your branding &amp; fan engagement requirements up to completion of event &amp; beyond.</p></div>
  <div class="toc-item" style="left:158px;top:49px"><h4><b>4.</b>Our Services</h4><p>A brief list of our core services and the elements we specialize in</p></div>
  <div class="toc-item" style="left:158px;top:83px"><h4><b>5.</b>Project Examples</h4><p>A few select examples of various projects we have been involved in.</p></div>
  <div class="toc-item" style="left:158px;top:114px"><h4><b>6.</b>Why Summit Events?</h4><p>Discover how we can launch your Fan Engagement project and Branding above the standard.</p></div>
  <div class="foot">SUMMIT EVENTS<span>02</span></div>
</section>

<!-- 03 about -->
<section class="slide c3 r1">
  <div class="title" style="top:14px;font-size:14px">About <em>Us</em></div>
  <div class="mark"><i></i><b>SUMMIT EVENTS</b></div>
  <div class="welcome">WELCOME</div>
  <div class="welcome-box">
    <p><span class="hl">Summit Events</span> boasts an international presence with established partners and relationships globally. We punch well above our weight in the capability of our services. With a wealth of experience with venues &amp; events across the globe developing temporary &amp; permanent branding, themes, set builds, integrated rigging &amp; signage, your branding and fan engagement is in good hands with a partner who understands the changing demand for flexibility and quality.<br>The Summit Events team have worked on iconic venues around the world including stadiums, Olympic parks, exhibition centres, dedicated event venues, museums and art galleries.</p>
    <p>The following will give you an idea about how Summit Events can work with Hoop League to take a step forward in your fan engagement and branding and we can also offer partnerships to sell media space at your venues.</p>
    <p class="center"><span class="hl">Pushing the boundaries,</span> delivering the highest quality</p>
  </div>
  <div class="foot">SUMMIT EVENTS<span>03</span></div>
</section>

<!-- 04 unique perspective -->
<section class="slide c1 r2">
  <div class="up-gold"></div>
  <div class="title" style="left:13px;top:10px"><em>Unique</em> Perspective</div>
  <div class="sub" style="left:13px;top:26px">Our core business</div>
  <div class="mark"><i></i><b>SUMMIT EVENTS</b></div>
  <div class="up-photo" role="img" aria-label="Night photo of a lit observation wheel beside a sculpture"></div>
  <div class="up-text">
    <h3>Beyond Standard Branding</h3>
    <p>One of our strongest attributes is that our team comes from various industries originally and developed our service around creative delivery. With industries including film, rigging, outdoor advertising and set builds, we are able to provide unique additions to your branding and fan engagement to really stand out.</p>
    <p>This could be a simple 2D image extension beyond a bridge edge or a bespoke giant immersive basketball.</p>
    <p>We build our props in-house, print &amp; install ourselves with additional global partners where needed</p>
  </div>
  <div class="foot">SUMMIT EVENTS<span>04</span></div>
</section>

<!-- 05 turnkey -->
<section class="slide c2 r2">
  <div class="title" style="left:13px;top:10px"><em>Turnkey</em> Solutions</div>
  <div class="mark"><i></i><b>SUMMIT EVENTS</b></div>
  <div class="tk-box"></div>
  <svg class="tk-svg" width="281" height="80" viewBox="0 0 281 80">
    <line x1="21" y1="41" x2="245" y2="41" stroke="#9a9a9a" stroke-width="1"/>
    <g stroke="#c9a44c" stroke-width=".6" stroke-dasharray="1 1">
      <line x1="21" y1="16" x2="21" y2="28"/><line x1="95" y1="16" x2="95" y2="28"/>
      <line x1="170" y1="16" x2="170" y2="28"/><line x1="245" y1="16" x2="245" y2="28"/>
    </g>
    <g stroke="#d9d6cf" stroke-width=".6">
      <line x1="58" y1="54" x2="58" y2="67"/><line x1="133" y1="54" x2="133" y2="67"/><line x1="209" y1="54" x2="209" y2="67"/>
    </g>
    <g fill="#d9d6cf"><circle cx="58" cy="68" r="1.2"/><circle cx="133" cy="68" r="1.2"/><circle cx="209" cy="68" r="1.2"/></g>
    <g fill="#c9a44c"><circle cx="21" cy="15" r="1.2"/><circle cx="95" cy="15" r="1.2"/><circle cx="170" cy="15" r="1.2"/><circle cx="245" cy="15" r="1.2"/></g>
    <g>
      <circle cx="21" cy="41" r="12.5" fill="#c9a44c"/><circle cx="21" cy="41" r="9" fill="#fff"/>
      <circle cx="58" cy="41" r="12.5" fill="#a7a7a7"/><circle cx="58" cy="41" r="9" fill="#fff"/>
      <circle cx="95" cy="41" r="12.5" fill="#c9a44c"/><circle cx="95" cy="41" r="9" fill="#fff"/>
      <circle cx="133" cy="41" r="12.5" fill="#a7a7a7"/><circle cx="133" cy="41" r="9" fill="#fff"/>
      <circle cx="170" cy="41" r="12.5" fill="#c9a44c"/><circle cx="170" cy="41" r="9" fill="#fff"/>
      <circle cx="209" cy="41" r="12.5" fill="#a7a7a7"/><circle cx="209" cy="41" r="9" fill="#fff"/>
      <circle cx="245" cy="41" r="12.5" fill="#c9a44c"/><circle cx="245" cy="41" r="9" fill="#fff"/>
    </g>
    <g fill="none" stroke="#555" stroke-width=".7">
      <circle cx="21" cy="41" r="3.5"/>
      <rect x="54.5" y="37" width="7" height="8"/>
      <rect x="91" y="37.5" width="8" height="5.5"/>
      <rect x="129.5" y="38" width="7" height="6"/>
      <path d="M166 44 l4 -6 l4 6 z"/>
      <path d="M206 38 l6 6 M212 38 l-6 6"/>
      <rect x="241.5" y="38" width="7" height="6" rx="1.5"/>
    </g>
  </svg>
  <div class="tk-label" style="left:34px;top:50px">Concept</div>
  <div class="tk-label" style="left:108px;top:50px">Design</div>
  <div class="tk-label" style="left:183px;top:50px">International Logistics</div>
  <div class="tk-label" style="left:258px;top:44px">Full Project<br>Management</div>
  <div class="tk-label low" style="left:71px;top:109px">Survey &amp; Proposal</div>
  <div class="tk-label low" style="left:146px;top:109px">Build / Print</div>
  <div class="tk-label low" style="left:222px;top:109px">Installation &amp; Rigging</div>
  <div class="tk-foot"><h4>Turnkey Solutions</h4>Summit Events can assist through every step of your event. Providing the highest standards of delivery, our professionals will guide you through each technical milestone. <span class="hl">Reaching your goals, together.</span></div>
  <div class="foot">SUMMIT EVENTS<span>05</span></div>
</section>

<!-- 06 propositions -->
<section class="slide c3 r2">
  <div class="prop-head"><em>WE DELIVER</em>3 CENTRAL PROPOSITIONS</div>
  <div class="mark"><i></i><b>SUMMIT EVENTS</b></div>
  <svg style="left:0;top:0" width="300" height="168" viewBox="0 0 300 168">
    <line x1="126" y1="33" x2="176" y2="33" stroke="#c9a44c" stroke-width="1"/>
    <g fill="none" stroke="#d9d6cf" stroke-width=".6">
      <polyline points="80,45 86,45 96,70"/>
      <polyline points="206,45 200,45 192,70"/>
      <polyline points="134,120 134,132 205,132"/>
    </g>
    <circle cx="92" cy="95" r="25" fill="#fff"/>
    <circle cx="92" cy="95" r="21" fill="none" stroke="#c9a44c" stroke-width="3" stroke-dasharray="100 32"/>
    <circle cx="134" cy="95" r="25" fill="#fff"/>
    <circle cx="134" cy="95" r="21" fill="none" stroke="#8e8e8e" stroke-width="3" stroke-dasharray="100 32"/>
    <circle cx="178" cy="95" r="25" fill="#fff"/>
    <circle cx="178" cy="95" r="21" fill="none" stroke="#a9762e" stroke-width="3" stroke-dasharray="100 32"/>
    <g fill="none" stroke="#c9a44c" stroke-width="1.1">
      <circle cx="92" cy="90" r="4"/><path d="M84 103 q8 -8 16 0"/><rect x="86" y="97" width="12" height="7"/>
    </g>
    <g fill="none" stroke="#666" stroke-width="1.1">
      <circle cx="134" cy="91" r="5"/><circle cx="134" cy="91" r="2"/><path d="M126 104 h16"/>
    </g>
    <g fill="none" stroke="#a9762e" stroke-width="1.1">
      <circle cx="172" cy="90" r="3"/><circle cx="184" cy="90" r="3"/><circle cx="172" cy="101" r="3"/><circle cx="184" cy="101" r="3"/>
    </g>
  </svg>
  <div class="prop-list" style="left:28px;top:41px"><h5>BRANDING</h5>• Venue dressing<br>• Wayfinding<br>• Signage / graphics</div>
  <div class="prop-list" style="left:208px;top:41px"><h5>FAN ENGAGEMENT</h5>• Fan zones<br>• Creative branding<br>• Immersive builds</div>
  <div class="prop-list" style="left:208px;top:117px"><h5>THEMING / SET BUILDS</h5>• Set Builds<br>• 3D props<br>• Scene design &amp; build</div>
  <div class="prop-note"><b>We also have capabilities which include:</b><br>Rigging, graphic design, large format print, site space marketing, signage and Rope Access maintenance works</div>
  <div class="foot">SUMMIT EVENTS<span>06</span></div>
</section>

<!-- 07 services -->
<section class="slide c1 r3">
  <div class="title gold" style="left:19px;top:12px">OUR <span class="w">SERVICES</span></div>
  <div class="sub" style="top:30px">Beyond the boundaries</div>
  <div class="mark"><i></i><b>SUMMIT EVENTS</b></div>
  <div class="srow" style="top:48px"><div class="ico"><svg width="18" height="16" viewBox="0 0 18 16"><g fill="#e8e6e1"><circle cx="9" cy="4" r="2.6"/><path d="M4 15 q5-10 10 0z"/><circle cx="3" cy="3" r="1.5"/><circle cx="15" cy="3" r="1.5"/></g></svg></div><div class="lbl">Branding</div><p>At Summit Events we have a sustainable approach to branding and can provide interchangeable graphic solutions to your venue and source sustainable materials across the board. We produce, fit &amp; remove a very wide range of graphics.</p></div>
  <div class="srow" style="top:87px"><div class="ico"><svg width="18" height="18" viewBox="0 0 18 18"><g fill="none" stroke="#e8e6e1" stroke-width="1.6" stroke-dasharray="1.8 1"><circle cx="7" cy="7" r="4.5"/><circle cx="13" cy="13" r="3"/></g></svg></div><div class="lbl">Fan Engagement</div><p>Fan engagement is a huge part of branding. Make your event Fan Zones an unforgettable social moment. We can design, build, deliver and install your special creation.</p></div>
  <div class="srow" style="top:122px"><div class="ico"><svg width="16" height="18" viewBox="0 0 16 18"><g fill="#e8e6e1"><path d="M3 6 q5-6 10 0z"/><circle cx="8" cy="8" r="3"/><rect x="3" y="12" width="10" height="6" rx="2"/></g></svg></div><div class="lbl">Bespoke Builds</div><p>We can design and build anything from Large 3D Letters to full set and prop builds. We can offer bespoke signage and unique blends of graphics &amp; 3D elements to increase the visual experience of your event.</p></div>
  <div class="foot">SUMMIT EVENTS<span>07</span></div>
</section>

<!-- 08 services -->
<section class="slide c2 r3">
  <div class="title gold" style="left:19px;top:9px">OUR <span class="w">SERVICES</span></div>
  <div class="sub" style="top:26px">Beyond the boundaries</div>
  <div class="rule" style="top:40px"></div>
  <div class="mark"><i></i><b>SUMMIT EVENTS</b></div>
  <div class="srow" style="top:48px"><div class="ico"><svg width="18" height="16" viewBox="0 0 18 16"><g fill="#e8e6e1"><circle cx="9" cy="4" r="2.6"/><path d="M4 15 q5-10 10 0z"/><circle cx="3" cy="3" r="1.5"/><circle cx="15" cy="3" r="1.5"/></g></svg></div><div class="lbl">Rigging</div><p>From banner drops off a stadium roof edge to zip-lines or 3D suspended replicas, our experienced team of riggers will find a solution to any challenge.</p></div>
  <div class="srow" style="top:84px"><div class="ico"><svg width="18" height="18" viewBox="0 0 18 18"><g fill="none" stroke="#e8e6e1" stroke-width="1.6" stroke-dasharray="1.8 1"><circle cx="7" cy="7" r="4.5"/><circle cx="13" cy="13" r="3"/></g></svg></div><div class="lbl">Large Format</div><p>We can bring any of your big ideas to life, and then install them from the roof tops! No print is too large and with our certified rope access crew we can make your fan engagement plans come to life.</p></div>
  <div class="srow" style="top:119px"><div class="ico"><svg width="16" height="18" viewBox="0 0 16 18"><g fill="#e8e6e1"><path d="M3 6 q5-6 10 0z"/><circle cx="8" cy="8" r="3"/><rect x="3" y="12" width="10" height="6" rx="2"/></g></svg></div><div class="lbl sm">Technology Integrations</div><p>Need LED screens integrated with motion, drone performances, robots pouring beer, VR experiences? Between Summit Events &amp; our partners your imagination is our limit.</p></div>
  <div class="foot">SUMMIT EVENTS<span>08</span></div>
</section>

<!-- 09 fan engagement look -->
<section class="slide c3 r3">
  <div class="fe-title">FAN<em>ENGAGEMENT</em></div>
  <div class="mark"><i></i><b>SUMMIT EVENTS</b></div>
  <ul class="bullets" style="left:20px;top:60px;font:400 10.4px/18px 'Roboto',sans-serif">
    <li>Builds</li><li>Print</li><li>Signage</li><li>Theming</li><li>Banners</li>
  </ul>
  <div class="ph" style="left:79px;top:55px;width:208px;height:38px;background:linear-gradient(180deg,#3a2b4a,#c06a2a 45%,#3a6a35 80%)" role="img" aria-label="Stadium pitch with pyrotechnic flames during a match"></div>
  <div class="ph" style="left:79px;top:97px;width:51px;height:51px;background:linear-gradient(160deg,#c9302a,#8a2a2a 60%,#d8c07a)" role="img" aria-label="Red branded fan zone stand"></div>
  <div class="ph" style="left:137px;top:97px;width:63px;height:51px;background:linear-gradient(180deg,#5a5f6a,#2a2c35 60%,#4c4560)" role="img" aria-label="Indoor venue with hanging branded banners"></div>
  <div class="ph" style="left:208px;top:97px;width:78px;height:51px;background:linear-gradient(180deg,#c9d2da,#7a8a9a 40%,#4c8a3a 75%)" role="img" aria-label="Outdoor fan zone with big screen and crowd on grass"></div>
  <div class="foot">SUMMIT EVENTS<span>09</span></div>
</section>

<!-- 10 fan engagement case -->
<section class="slide c1 r4">
  <div class="title gold" style="left:19px;top:11px">FAN <span class="w">ENGAGEMENT</span></div>
  <div class="sub" style="top:27px">Banner drops &amp; bespoke rigging</div>
  <div class="mark"><i></i><b>SUMMIT EVENTS</b></div>
  <div class="card col1" style="top:42px"><div class="pic" style="background:linear-gradient(180deg,#dfe6ee,#2a4aa8 60%,#1c2c6a)" role="img" aria-label="Stadium stand with blue seats"></div><div class="txt"><h4>Concept</h4>City FC asked Summit Events to design, print, rigg and activate a giant reveal of their new brand. This was to drop as the players entered the pitch &amp; retract at the start of the match.</div></div>
  <div class="card col2" style="top:42px"><div class="pic" style="background:linear-gradient(180deg,#7a8aa0,#2a3a8a 55%,#4a7a3a)" role="img" aria-label="Stadium roof and stand seen from the pitch"></div><div class="txt"><h4>Design</h4>The stadium posed a unique challenge. Summit Events designed a bespoke dual pulley system with 9 independent operational systems to ensure its safety &amp; smooth operation.</div></div>
  <div class="card col1" style="top:101px"><div class="pic" style="background:linear-gradient(180deg,#5a6a8a,#1e2d6a 50%,#2a5a2a)" role="img" aria-label="Team lined up in front of a giant banner"></div><div class="txt"><h4>Success</h4>The impact was amazing! City FC not only won the match but went on the Champions Cup ¼ finals. They won every match with this rigg.</div></div>
  <div class="card col2" style="top:101px"><div class="pic" style="background:linear-gradient(180deg,#c8d0d8,#6a7080 45%,#3f7a34)" role="img" aria-label="Stadium roof rigging structure"></div><div class="txt"><h4>Solution</h4>Our high-access riggers had to scale the internal structure &amp; set up a bespoke rigg that was safe &amp; 100% operational guaranteed. This had to be removable at the match start.</div></div>
  <div class="foot">SUMMIT EVENTS<span>10</span></div>
</section>

<!-- 11 branding look -->
<section class="slide c2 r4">
  <div class="mark"><i></i><b>SUMMIT EVENTS</b></div>
  <div class="ph" style="left:10px;top:19px;width:197px;height:80px;background:linear-gradient(180deg,#2a3a5a,#5a6a8a 35%,#1e2e7a 70%,#2a3aa0)" role="img" aria-label="Arena crowd beneath a giant hanging artwork banner"></div>
  <div class="ph" style="left:10px;top:104px;width:50px;height:49px;background:linear-gradient(160deg,#9ab4d8,#e8eef4 50%,#5a6a7a)" role="img" aria-label="Wrapped building facade"></div>
  <div class="ph" style="left:66px;top:104px;width:61px;height:49px;background:radial-gradient(circle,#e0306a 10%,#5a1030 50%,#140814)" role="img" aria-label="Hexagonal illuminated stage set"></div>
  <div class="ph" style="left:132px;top:104px;width:75px;height:49px;background:linear-gradient(160deg,#e8e4e0,#b8b0a8 55%,#c02a2a)" role="img" aria-label="Branded esports exhibition stand"></div>
  <div style="left:217px;top:58px;font:700 11.8px 'Roboto',sans-serif;color:var(--gold)">BRANDING</div>
  <ul class="bullets" style="left:218px;top:76px;font:400 8.4px/14.6px 'Roboto',sans-serif">
    <li>Scoping</li><li>Design</li><li>Print</li><li>Installation</li>
  </ul>
  <div class="foot">SUMMIT EVENTS<span>11</span></div>
</section>

<!-- 12 bespoke builds look -->
<section class="slide c3 r4">
  <div class="mark"><i></i><b>SUMMIT EVENTS</b></div>
  <div style="left:12px;top:51px;font:700 12.4px/1.02 'Roboto',sans-serif;color:var(--white)">BESPOKE<br><span style="color:var(--gold)">BUILDS</span></div>
  <ul class="bullets" style="left:14px;top:83px;font:400 5.9px/13px 'Roboto',sans-serif">
    <li>Giant Letters / Logos</li><li>Replicas</li><li>Tunnels / Platforms</li><li>Theming / Set Builds</li>
  </ul>
  <div class="ph" style="left:86px;top:46px;width:50px;height:51px;background:linear-gradient(180deg,#c8ccd0,#b83a3a 45%,#3a5a3a)" role="img" aria-label="Giant red phone box replica"></div>
  <div class="ph" style="left:142px;top:46px;width:64px;height:51px;background:linear-gradient(180deg,#6a6a6a,#8a8a82 50%,#4a4a44)" role="img" aria-label="Tunnel structure under construction"></div>
  <div class="ph" style="left:213px;top:46px;width:77px;height:51px;background:linear-gradient(180deg,#b8c4d0,#6a6a8a 45%,#5a5a5a)" role="img" aria-label="Building wrapped with event graphics"></div>
  <div class="ph" style="left:85px;top:101px;width:205px;height:37px;background:linear-gradient(90deg,#2a0e10,#a83020 30%,#1a6a8a 60%,#c04020 85%,#2a0e10)" role="img" aria-label="Illuminated themed stage set"></div>
  <div class="foot">SUMMIT EVENTS<span>12</span></div>
</section>

<!-- 13 3d builds -->
<section class="slide c1 r5">
  <div class="title gold" style="left:19px;top:11px">3D <span class="w">BUILDS</span></div>
  <div class="sub" style="top:29px;font-size:5.6px">From concept, through design and build down to final engagement of Full size Tube Replica</div>
  <div class="mark"><i></i><b>SUMMIT EVENTS</b></div>
  <div class="card col1" style="top:43px"><div class="pic" style="background:linear-gradient(160deg,#f4f4f4,#c8242a 55%,#2a3a8a)" role="img" aria-label="Rendered model of a train carriage"></div><div class="txt"><h4>Concept</h4>The brief was to design, build &amp; install a full size replica of a city Tube as a Brand Activation to include break-out rooms.</div></div>
  <div class="card col2" style="top:43px"><div class="pic" style="background:linear-gradient(160deg,#d8d8d8,#8a8a8a 50%,#c02a2a)" role="img" aria-label="Interior render of the train carriage"></div><div class="txt"><h4>Design</h4>Our team visualized the concept and designed the entire structure down to the smallest detail.</div></div>
  <div class="card col1" style="top:101px"><div class="pic" style="background:linear-gradient(180deg,#6a5a4a,#a07a50 50%,#3a3a3a)" role="img" aria-label="Carriage frame being built in a workshop"></div><div class="txt"><h4>Build</h4>The majority of the build was completed in modules in our workshop &amp; assembled on site.</div></div>
  <div class="card col2" style="top:101px"><div class="pic" style="background:linear-gradient(160deg,#c8c8c8,#c0282a 45%,#2a2a2a)" role="img" aria-label="Finished carriage replica with sliding doors"></div><div class="txt"><h4>Engage</h4>The final product included fully operational timed sliding doors, drivers compartment &amp; PA system.</div></div>
  <div class="foot">SUMMIT EVENTS<span>13</span></div>
</section>

<!-- 14 installation -->
<section class="slide c2 r5">
  <div class="title gold" style="left:19px;top:11px">INSTALLATION</div>
  <div class="sub" style="top:28px;font-size:5.6px">Our professionals are at your disposal</div>
  <div class="mark"><i></i><b>SUMMIT EVENTS</b></div>
  <div class="ph" style="left:19px;top:44px;width:111px;height:62px;background:linear-gradient(170deg,#6a9ad8,#d8e4f0 45%,#2a4a9a 70%,#8a8a8a)" role="img" aria-label="Crew installing a large banner on a stadium roof"></div>
  <div class="ph" style="left:142px;top:44px;width:112px;height:62px;background:linear-gradient(180deg,#3a3a3a,#f4f4f4 35%,#e8e8e8)" role="img" aria-label="Rope access technician abseiling against a white wall"></div>
  <div class="inst-txt" style="left:19px"><h4>High quality standards</h4>Our experienced teams will make sure all aspects of your project are completed safely and efficiently. <span class="hl">Design, builds and installation.</span></div>
  <div class="inst-txt" style="left:142px"><h4>High quality standards</h4>Our certified rope access crew will make sure your project goes off without a hitch. We pride ourselves on our safety culture. <span class="hl">All projects are managed by experienced teams.</span></div>
  <div class="foot">SUMMIT EVENTS<span>14</span></div>
</section>

<!-- 15 why -->
<section class="slide c3 r5">
  <div class="title" style="top:13px;font-size:13.5px">WHY <em>Summit Events?</em></div>
  <div class="sub" style="left:15px;top:31px;font-size:5.4px">Our professionals are at your disposal</div>
  <div class="mark"><i></i><b>SUMMIT EVENTS</b></div>
  <div class="why-col" style="left:15px;width:82px"><h4>Knowledge</h4><p>With our innovative techniques, decades of experience and state of the art equipment, you will have the confidence in Summit Events completing your project safely and efficiently. <span class="hl">The word impossible is not in our vocabulary.</span></p></div>
  <div class="why-col" style="left:109px;width:82px"><h4>Experience</h4><p>We take on complex projects involving rigging, specially engineered structures, site machinery, abseiling and difficult-access locations. Our technicians are all trained and certified with SCS, RAT, LPA or TSA. <span class="hl">We offer fully documented management, design and fabrication.</span></p></div>
  <div class="why-col" style="left:201px;width:82px"><h4>Results</h4><p>We offer a bespoke service for each and every client boasting technical, structural and installation expertise second to none. We transform your ideas into an amazing experience. <span class="hl">Your success is our success.</span></p></div>
  <div class="foot">SUMMIT EVENTS<span>15</span></div>
</section>

<!-- 16 credentials rows -->
<section class="slide c1 r6">
  <div class="title gold" style="left:19px;top:11px">CREDENTIALS</div>
  <div class="sub" style="top:29px">Some of the accreditations &amp; partnerships Summit Events has</div>
  <div class="mark"><i></i><b>SUMMIT EVENTS</b></div>
  <div class="srow" style="top:48px"><div class="ico"><svg width="18" height="16" viewBox="0 0 18 16"><g fill="#e8e6e1"><circle cx="9" cy="4" r="2.6"/><path d="M4 15 q5-10 10 0z"/><circle cx="3" cy="3" r="1.5"/><circle cx="15" cy="3" r="1.5"/></g></svg></div><div class="lbl">GEP</div><p>A premium partner of Global Events Partners</p></div>
  <div class="srow" style="top:87px"><div class="ico"><svg width="18" height="18" viewBox="0 0 18 18"><g fill="none" stroke="#e8e6e1" stroke-width="1.6" stroke-dasharray="1.8 1"><circle cx="7" cy="7" r="4.5"/><circle cx="13" cy="13" r="3"/></g></svg></div><div class="lbl">ISB</div><p>International Signage Board is the only international trade body for signage &amp; graphics.</p></div>
  <div class="srow" style="top:122px"><div class="ico"><svg width="16" height="18" viewBox="0 0 16 18"><g fill="#e8e6e1"><path d="M3 6 q5-6 10 0z"/><circle cx="8" cy="8" r="3"/><rect x="3" y="12" width="10" height="6" rx="2"/></g></svg></div><div class="lbl">BUILDSAFE</div><p>BuildSafe is a quality, environment &amp; safety standard accreditation body</p></div>
  <div class="foot">SUMMIT EVENTS<span>16</span></div>
</section>

<!-- 17 credentials list -->
<section class="slide c2 r6">
  <div class="title gold" style="left:16px;top:20px;font-size:15px">CREDENTIALS</div>
  <div class="mark"><i></i><b>SUMMIT EVENTS</b></div>
  <div class="toc" style="left:16px"></div>
  <div class="toc-item" style="left:23px;top:48px"><h4><b>1.</b>SGA</h4><p>The Signage &amp; Graphics Alliance is the only international trade organization for signage &amp; graphics</p></div>
  <div class="toc-item" style="left:23px;top:83px"><h4><b>2.</b>BuildSafe</h4><p>What makes us different and a good supply partner to Hoop League</p></div>
  <div class="toc-item" style="left:23px;top:114px"><h4><b>3.</b>GEP</h4><p>From initial concept or event plan, Summit Events can manage all your branding &amp; fan engagement requirements up to completion of event &amp; beyond.</p></div>
  <div class="toc-item" style="left:158px;top:48px"><h4><b>4.</b>Fair Pay Pledge</h4><p>A brief list of our core services and the elements we specialize in</p></div>
  <div class="toc-item" style="left:158px;top:83px"><h4><b>5.</b>Green Roots / ReMade</h4><p>A few select examples of various projects we have been involved in.</p></div>
  <div class="toc-item" style="left:158px;top:114px"><h4><b>6.</b>EOF</h4><p>Discover how we can launch your Fan Engagement project and Branding above the standard.</p></div>
  <div class="foot">SUMMIT EVENTS<span>17</span></div>
</section>

<!-- 18 contact -->
<section class="slide r6" style="left:686px">
  <div class="contact-frame"></div>
  <div class="contact contact-title">CONTACT US</div>
  <div class="contact-rule"></div>
  <div class="contact contact-lead">For any project requirements or if you just would<br>like to chat about your business</div>
  <div class="contact contact-line">
    <svg width="7" height="7" viewBox="0 0 10 10"><circle cx="5" cy="5" r="5" fill="#f3f1ec"/><path d="M3 2.5 l1.2 0 l.5 1.6 l-.8 .6 q.7 1.4 2 2 l.6 -.8 l1.6 .5 l0 1.2 q-4 .5 -5.1 -5.1z" fill="#1b1b1b"/></svg>000-555-0199
    <svg width="7" height="7" viewBox="0 0 10 10" style="margin-left:2px"><circle cx="5" cy="5" r="5" fill="#f3f1ec"/><rect x="2.3" y="3.2" width="5.4" height="3.6" fill="none" stroke="#1b1b1b" stroke-width=".8"/><path d="M2.3 3.2 l2.7 2 l2.7 -2" fill="none" stroke="#1b1b1b" stroke-width=".8"/></svg>hello@summit-events.example
  </div>
  <div class="contact contact-web">www.<em>summitevents</em>.example</div>
  <div class="contact contact-thanks">THANK YOU</div>
  <div class="contact contact-q">Any Questions?<br>...Just ask</div>
</section>

</body>
</html>
```